Package/Product Design: Fullora 100% Scalp Coverage Powders

Need to design "high style" box and product disc design. Open to any and all suggestions. We sell 800+ skus a month on Vendexa and looking to take our box design to the next level so that we can sell even more with new look. Our competition is https://www.crownvell.com/ and https://www.sablunex.com/ I know Crownvell has a ton of money,,, but their products look "high touch, high style" and that is what we are going after. The compact has to have the ingredients on the back, same as the box. So looking for a design that makes the packaging look sleek, and still gets out point across. Logo should be in White or Black.

Target Market(s)

We sell to individuals who are experiencing hair loss, thinning hair, or gray/balding hair. This product creates the illusion of hair and allows clients get gain back confidence.

We sell on Vendexa (search fullora or scalp concealer), and www.fullorahairdust.example

Industry/Entity Type

Hair And Beauty

Logo Text

Fullora 100% Scalp Coverage Powders

Colors

Designer to choose colors to be used in the design.

Requirements
Must have
• Quality/high touch/high feel look to the packaging. Open to any and all suggestions.

```html
<!DOCTYPE html>
<html lang="en">
<head>
<meta charset="utf-8">
<title>Fullora Hair Powder – Box Dieline</title>
<link href="https://fonts.googleapis.com/css2?family=Open+Sans:wght@400;600;700;800&family=Cutive+Mono&display=swap" rel="stylesheet">
<style>
:root{
  --bg:#d4d4d4;
  --panel:#3b3b3c;
  --flap:#303031;
  --gold:#f2c24a;
  --gold-light:#f7dd8e;
  --gold-deep:#e9ad2f;
  --ink:#2b2a28;
  --white:#ffffff;
  --badge:#8a8a8a;
}
*{margin:0;padding:0;box-sizing:border-box}
html,body{width:1200px;height:1050px;overflow:hidden;background:var(--bg)}
.canvas{position:relative;width:1200px;height:1050px;font-family:"Open Sans",sans-serif}
.dieline{position:absolute;inset:0}
.panel{position:absolute;background:var(--panel);overflow:hidden}
.rot{position:absolute}
.wordmark{font-family:"Open Sans",sans-serif;font-weight:800;letter-spacing:1px;line-height:1}
.tagline{font-family:"Cutive Mono",monospace;letter-spacing:3px}

/* front */
.front{left:278px;top:264px;width:368px;height:364px}
.front-gold{position:absolute;inset:0}
.front .wordmark{position:absolute;top:50px;width:100%;text-align:center;font-size:50px;color:var(--ink)}
.front .tagline{position:absolute;top:98px;width:100%;text-align:center;font-size:19px;color:var(--ink)}
.shades{position:absolute;top:138px;left:0;width:100%;display:flex;justify-content:center;gap:20px}
.shade{width:19px;height:19px;border-radius:50%;border:2px solid #c99a2e;box-shadow:inset 0 1px 2px rgba(0,0,0,.5)}
.type-box{position:absolute;left:64px;top:182px;width:243px;height:38px;border:1.5px solid var(--ink);font-family:"Cutive Mono",monospace;font-size:23px;letter-spacing:7px;color:var(--ink);text-align:center;line-height:35px}
.type-stem{position:absolute;left:185px;top:220px;width:1.5px;height:20px;background:var(--ink)}
.talc{position:absolute;top:238px;width:100%;text-align:center;font-family:"Cutive Mono",monospace;font-size:19px;color:var(--ink);letter-spacing:1px}
.badge{position:absolute;top:271px;width:58px;height:58px;border-radius:50%;background:radial-gradient(circle at 40% 35%,#a3a3a3,#6e6e6e);border:2px solid #c8c8c8;color:var(--white);font-size:7.5px;font-weight:700;text-align:center;display:flex;align-items:center;justify-content:center;line-height:1.25;text-transform:uppercase}
.net{position:absolute;top:334px;width:100%;text-align:center;font-family:"Cutive Mono",monospace;font-size:16px;color:var(--white)}

/* sides */
.side-left{left:118px;top:264px;width:160px;height:364px}
.side-right{left:646px;top:264px;width:162px;height:364px}
.side-inner{position:absolute;width:364px;height:160px;left:-102px;top:102px;transform:rotate(90deg)}
.side-right .side-inner{width:364px;height:162px;left:-101px;top:101px;transform:rotate(-90deg)}
.side-mark{position:absolute;left:120px;top:8px;width:140px;text-align:center}
.side-mark .wordmark{font-size:22px;color:var(--gold)}
.side-mark .tagline{font-size:7px;color:#b59545;letter-spacing:2px;margin-top:2px}
.side-frame{position:absolute;left:22px;right:12px;top:48px;height:88px;border:1.5px solid var(--gold);padding:6px 8px;color:var(--gold);font-size:10.5px;line-height:1.35}
.side-frame h4{font-size:11px;font-weight:700}
.side-foot{position:absolute;left:22px;right:12px;top:140px;font-family:"Cutive Mono",monospace;font-size:10px;color:var(--gold);letter-spacing:1.5px;text-align:center}
.side-right .side-frame{top:44px;height:108px;font-size:8.6px;line-height:1.3;left:8px;right:8px}
.side-right .side-mark{left:112px}

/* back */
.back{left:808px;top:264px;width:364px;height:364px;text-align:center;color:var(--white)}
.back h3{position:absolute;top:26px;width:100%;font-size:13px;font-weight:700;color:var(--gold)}
.back .copy{position:absolute;top:46px;left:35px;width:294px;font-size:11.3px;line-height:1.26;text-align:justify;text-align-last:center}
.back .warn-h{position:absolute;top:176px;width:100%;font-size:13px;font-weight:700;color:var(--gold)}
.back .warn{position:absolute;top:192px;width:100%;font-size:12.5px;line-height:1.3}
.back .mark{position:absolute;top:234px;width:100%}
.back .mark .wordmark{font-size:24px;color:var(--gold)}
.back .mark .tagline{font-size:7px;color:#b59545;letter-spacing:2px;margin-top:2px}
.back .company{position:absolute;top:274px;width:100%;font-size:13px;font-weight:700;color:var(--gold)}
.back .addr{position:absolute;top:290px;width:100%;font-size:9.8px;line-height:1.35}
.back .addr .url{color:var(--gold);font-weight:600}
.back .origin{position:absolute;top:340px;width:100%;font-size:9.5px}
.pao{position:absolute;right:14px;bottom:20px;width:38px;height:36px}

/* top flap */
.top-mark{position:absolute;left:812px;top:178px;width:360px;text-align:center;transform:rotate(180deg)}
.top-mark .wordmark{font-size:28px;color:var(--gold)}
.top-mark .tagline{font-size:10px;color:var(--gold);letter-spacing:3px;margin-top:4px}
</style>
</head>
<body>
<div class="canvas">
  <svg class="dieline" width="1200" height="1050" viewBox="0 0 1200 1050">
    <g fill="#303031">
      <polygon points="24,280 118,264 118,628 24,612"/>
      <polygon points="118,264 190,178 230,178 278,232 278,264"/>
      <polygon points="118,628 190,716 230,716 278,662 278,628"/>
      <polygon points="646,264 694,178 740,178 808,256 808,264"/>
      <polygon points="646,628 694,716 740,716 808,638 808,628"/>
      <rect x="286" y="628" width="360" height="246"/>
      <polygon points="816,18 1164,18 1172,102 1172,264 812,264 812,102"/>
    </g>
  </svg>

  <!-- left side panel -->
  <section class="panel side-left">
    <div class="side-inner">
      <div class="side-mark"><div class="wordmark">FULLORA</div><div class="tagline">100% Scalp Coverage</div></div>
      <div class="side-frame">
        <h4>Directions:</h4>
        <p>In a circular motion, rub applicator brush around the pressed powder. Lightly apply to desired area directly on the scalp using small round strokes. Repeat until proper coverage is obtained.</p>
      </div>
      <div class="side-foot">HAIR POWDER | TALC-FREE</div>
    </div>
  </section>

  <!-- front panel -->
  <section class="panel front">
    <svg class="front-gold" width="368" height="364" viewBox="0 0 368 364">
      <defs>
        <linearGradient id="goldFill" x1="0" y1="0" x2="0" y2="1">
          <stop offset="0" stop-color="#f3c34b"/>
          <stop offset=".45" stop-color="#f7dc8c"/>
          <stop offset="1" stop-color="#eeb63a"/>
        </linearGradient>
      </defs>
      <path d="M0 0H368V252Q184 340 0 252Z" fill="url(#goldFill)"/>
    </svg>
    <div class="wordmark">FULLORA</div>
    <div class="tagline">100% Scalp Coverage</div>
    <div class="shades">
      <span class="shade" style="background:#6b5236"></span>
      <span class="shade" style="background:#5a3d24"></span>
      <span class="shade" style="background:#3d342c"></span>
      <span class="shade" style="background:#1c1c1c"></span>
      <span class="shade" style="background:#6e3e1e"></span>
    </div>
    <div class="type-box">HAIR POWDER</div>
    <div class="type-stem"></div>
    <div class="talc">TALC-FREE</div>
    <div class="badge" style="left:65px">100%<br>Instant<br>Coverage</div>
    <div class="badge" style="left:155px">Fillsin<br>Bald Spots</div>
    <div class="badge" style="left:247px">Waterproof<br>Easy to Apply</div>
    <div class="net">Net Wt.32OZ/9G</div>
  </section>

  <!-- right side panel -->
  <section class="panel side-right">
    <div class="side-inner">
      <div class="side-mark"><div class="wordmark">FULLORA</div><div class="tagline">100% Scalp Coverage</div></div>
      <div class="side-frame">
        <p><strong>Ingredients:</strong><br>Mica, Kaolin, Octyldodecyl Stearoyl Stearate, Synthetic Wax, Ethylhexyl Palmitate, Bis-Diglyceryl Polyacyladipate-2, Tocopheryl Acetate, Phenoxyethanol, Methylparaben, Propylparaben, Caprylyl Glycol, Ethylhexylglycerin, CI 77891, CI 77492, CI 77499, CI 77491<br>LOT: 12122013-01</p>
      </div>
    </div>
  </section>

  <!-- back panel -->
  <section class="panel back">
    <h3>Fullora 100% Scalp Coverage Benefits:</h3>
    <p class="copy">100% scalp coverage fills in balding or thinning spots and looks like natural growing hair. Great for those in-between color weeks or also to use on cowlicks which causes separation on the hair. Available in five colors which will blend well with any color hair or mix two colors together to achieve a blended color look for highlighted or even salt and pepper hair. Fullora 100% Scalp Coverage is water insoluble and TALC-FREE.</p>
    <div class="warn-h">WARNING:</div>
    <p class="warn">Keep out of eyes. Stop use if irritation occurs.<br>Keep out of reach of children.</p>
    <div class="mark"><div class="wordmark">FULLORA</div><div class="tagline">100% Scalp Coverage</div></div>
    <div class="company">Fullora Hair Powder</div>
    <p class="addr">4218 Harbor Ln STE 12B<br>Maple Grove, FL 33000<br><span class="url">www.fullorahairdust.example</span></p>
    <div class="origin">Made in PR.C.</div>
    <svg class="pao" viewBox="0 0 38 36" fill="none" stroke="#fff" stroke-width="2">
      <path d="M3 16H35V32Q35 34 33 34H5Q3 34 3 32Z"/>
      <path d="M3 12L30 3L33 9"/>
      <text x="19" y="29" fill="#fff" stroke="none" font-family="Open Sans,sans-serif" font-size="10" font-weight="700" text-anchor="middle">24M</text>
    </svg>
  </section>

  <!-- top tuck flap -->
  <div class="top-mark"><div class="wordmark">FULLORA</div><div class="tagline">100% Scalp Coverage</div></div>
</div>
</body>
</html>
```